the halvorsen group premier division

design a DL A4 tri fold brochure to reflect our creative landscape business
my web site www.thehalvorsengroup.com.au
has all the information needed
i will also be updating the website to be more updated and creative design

```html
<!DOCTYPE html>
<html lang="en">
<head>
<meta charset="utf-8">
<title>The Halvorsen Group – DL Tri-fold Front</title>
<link rel="stylesheet" href="https://fonts.googleapis.com/css2?family=Arimo:ital,wght@0,400;0,700;1,400&family=Roboto+Condensed:wght@400&family=Varela+Round&display=swap">
<style>
  :root {
    --page-bg: #ffffff;
    --ink: #1c1c1c;
    --ink-soft: #3a3a3a;
    --orange: #f0922a;
    --teal-pale: #dcebe8;
    --teal-mid: #b8d8d2;
    --grey-pale: #eeeeee;
    --box-bg: rgba(255, 255, 255, 0.72);
    --dash: #111111;
  }
  * { box-sizing: border-box; margin: 0; padding: 0; }
  html, body { width: 1143px; height: 1200px; overflow: hidden; background: var(--page-bg); }
  body { position: relative; font-family: "Arimo", Arial, sans-serif; color: var(--ink); }

  .panel { position: absolute; left: 17px; width: 1108px; overflow: hidden; }

  /* Cover panel */
  .cover { top: 17px; height: 367px; }
  .cover-photo {
    position: absolute; inset: 0;
    background:
      linear-gradient(90deg, rgba(150,155,160,0.55) 0%, rgba(150,155,160,0) 45%),
      linear-gradient(180deg, #5f7c4a 0%, #8fa07a 30%, #a9aea8 55%, #8d9189 80%, #6f6a5e 100%);
  }
  .headline {
    position: absolute; right: 62px; top: 52px;
    font-family: "Varela Round", Arial, sans-serif;
    font-size: 47px; font-weight: 400; color: var(--orange);
    text-shadow: 1px 1px 2px rgba(0,0,0,0.55);
  }
  .brand { position: absolute; left: 101px; top: 200px; }
  .brand-dot {
    width: 62px; height: 62px; border-radius: 50%;
    background: var(--orange); margin: 0 0 14px 110px;
  }
  .brand-name { font-size: 34px; font-weight: 700; color: var(--ink-soft); line-height: 1; }
  .brand-division {
    font-size: 14px; letter-spacing: 3px; color: var(--ink-soft);
    margin: 8px 0 0 80px;
  }
  .web {
    position: absolute; right: 21px; top: 328px;
    font-size: 30px; font-weight: 700; color: var(--ink);
  }

  .fold-line {
    position: absolute; left: 17px; width: 1108px; height: 0;
    border-top: 2px dashed var(--dash);
  }
  .fold-1 { top: 386px; }
  .fold-2 { top: 763px; }

  /* Services panel */
  .services { top: 390px; height: 370px; }
  .services-art {
    position: absolute; inset: 0;
    background:
      radial-gradient(ellipse 60% 40% at 30% 100%, rgba(190,215,150,0.7), rgba(190,215,150,0) 70%),
      radial-gradient(ellipse 40% 50% at 85% 85%, rgba(140,200,190,0.6), rgba(140,200,190,0) 70%),
      linear-gradient(180deg, #eef1f0 0%, var(--teal-pale) 60%, var(--teal-mid) 100%);
  }
  .services-title {
    position: absolute; left: 66px; top: 8px;
    font-size: 30px; font-weight: 700; color: var(--ink); letter-spacing: -0.3px;
  }
  .services-title small { font-size: 20px; }
  .service-list { position: absolute; left: 115px; top: 62px; font-size: 19px; line-height: 23.7px; }
  .service-group { font-size: 22px; font-weight: 700; line-height: 23.7px; }
  .service-list ul { list-style: none; margin-left: 14px; }
  .service-list li { position: relative; padding-left: 32px; }
  .service-list li::before {
    content: ""; position: absolute; left: 0; top: 10px;
    width: 4px; height: 4px; background: var(--ink); border-radius: 50%;
  }
  .intro-box {
    position: absolute; left: 594px; top: 84px; width: 486px; height: 216px;
    background: var(--box-bg); border-radius: 12px;
    padding: 14px 22px; font-style: italic; font-size: 17px; line-height: 18.6px; color: var(--ink-soft);
  }
  .intro-box p + p { margin-top: 18px; }

  /* Project panel */
  .project { top: 767px; height: 366px; background: linear-gradient(180deg, #f6f6f6, var(--grey-pale)); }
  .project-title { position: absolute; left: 48px; top: 62px; font-size: 21px; font-weight: 700; }
  .project-tagline { position: absolute; left: 48px; top: 110px; font-size: 21px; font-style: italic; }
  .project-label { position: absolute; left: 48px; top: 162px; font-size: 19px; }
  .project-details { position: absolute; left: 48px; top: 193px; list-style: none; font-size: 19px; line-height: 31.5px; }
  .project-details li::before { content: "• "; }
  .project-photo {
    position: absolute; left: 643px; top: 14px; width: 442px; height: 331px;
    background: linear-gradient(180deg, #9fb4c8 0%, #d8dadb 35%, #8f9290 65%, #5f6b4e 100%);
  }

  .caption {
    position: absolute; left: 0; width: 1143px; top: 1145px; text-align: center;
    font-family: "Roboto Condensed", Arial, sans-serif; font-size: 29px; color: var(--ink);
  }
</style>
</head>
<body>

<section class="panel cover">
  <div class="cover-photo" role="img" aria-label="Photograph of a modern garden patio with outdoor lounge, white chairs, stepping-stone paving and lawn"></div>
  <h1 class="headline">Landscaping to your Lifestyle</h1>
  <div class="brand">
    <div class="brand-dot"></div>
    <div class="brand-name">The Halvorsen Group</div>
    <div class="brand-division">PREMIER DIVISION</div>
  </div>
  <div class="web">www.thehalvorsengroup.com.au</div>
</section>

<div class="fold-line fold-1"></div>

<section class="panel services">
  <div class="services-art" role="img" aria-label="Soft illustration of pale teal trees, palms and rolling garden shapes"></div>
  <h2 class="services-title">LANDSCAPE CONSULTING <small>AND</small> DESIGN</h2>
  <div class="service-list">
    <div class="service-group">Construction</div>
    <ul>
      <li>Bespoke Structural Features</li>
      <li>Water Features</li>
      <li>Paving &amp; Pathways</li>
      <li>Concreting and Aggregate</li>
    </ul>
    <div class="service-group">Garden</div>
    <ul>
      <li>Plant &amp; Tree supply &amp; installation</li>
      <li>Earth Preparation</li>
      <li>Lawns</li>
      <li>Irrigation Systems</li>
    </ul>
    <div class="service-group">Maintenance</div>
    <ul>
      <li>Garden &amp; Structural</li>
    </ul>
  </div>
  <div class="intro-box">
    <p>The Halvorsen Group is delighted to share just some of the versatile landscapes that we have managed and constructed. As you will see, we take pride in delivering quality beautiful landscapes of various styles with exceptional attention to detail.</p>
    <p>Our team proves to share a passion for their work and ensures each client can experience an inviting and nurturing and yet functional outdoor living space.</p>
  </div>
</section>

<div class="fold-line fold-2"></div>

<section class="panel project">
  <h3 class="project-title">WILLIAMSTOWN PROJECT</h3>
  <p class="project-tagline">Strong and Soft Accents</p>
  <p class="project-label">Project Details:</p>
  <ul class="project-details">
    <li>Steel Arbor Entrance softened with constrasting roses</li>
    <li>Bluestone paving</li>
    <li>Pathway lined planting</li>
  </ul>
  <div class="project-photo" role="img" aria-label="Photograph of a steel arbor entrance covered in red roses over a bluestone path leading to a red door"></div>
</section>

<p class="caption">DL Tri-fold - Z Style - Front</p>

</body>
</html>
```